Verra needs a new design we have an updated logo and want a high qualitative high end feel

feel and aesthetic should be high qualitative like the packaging in a zuvi or the qualatative weight/feel of an zuvi design. modern, elegant bold.probably just the verra logo on the backone vesion could be blue background white letter ... open to ideas
Target Market(s)
legal, insurance , medical, finance rho 740
Industry/Entity Type
Information Technology
Font styles to use
Serif

```html
<!DOCTYPE html>
<html lang="en">
<head>
<meta charset="utf-8">
<title>Verra Business Card</title>
<link href="https://fonts.googleapis.com/css2?family=Lato:wght@400;700&display=swap" rel="stylesheet">
<style>
  :root {
    --navy: #1b2b3f;
    --white: #ffffff;
    --grey-text: #7a7a7a;
    --backdrop: #e6e4e1;
    --rule: #1b2b3f;
  }
  * { margin: 0; padding: 0; box-sizing: border-box; }
  html, body {
    width: 1200px; height: 848px; overflow: hidden;
    background: var(--backdrop);
    font-family: 'Lato', sans-serif;
  }
  .canvas { position: relative; width: 1200px; height: 848px; }
  .card {
    position: absolute; width: 674px; height: 378px;
    border-radius: 22px; overflow: hidden;
    box-shadow: 0 6px 16px rgba(0,0,0,0.18);
  }
  .card-back { left: 251px; top: 28px; background: var(--navy); }
  .card-front { left: 250px; top: 441px; height: 374px; background: var(--white); }

  .wordmark {
    position: absolute; display: flex; align-items: flex-start; gap: 6px;
    font-weight: 700; letter-spacing: 1px; line-height: 1;
  }
  .wordmark .dot { border-radius: 50%; }
  .card-back .wordmark { left: 0; right: 0; justify-content: center; top: 130px; color: var(--white); font-size: 110px; }
  .card-back .wordmark .dot { width: 14px; height: 14px; background: var(--white); margin-top: 18px; }
  .card-front .wordmark { left: 58px; top: 135px; color: var(--navy); font-size: 76px; }
  .card-front .wordmark .dot { width: 10px; height: 10px; background: var(--navy); margin-top: 12px; }

  .divider { position: absolute; left: 343px; top: 96px; width: 1.5px; height: 182px; background: var(--rule); }

  .details { position: absolute; left: 370px; top: 92px; color: var(--grey-text); }
  .details .name { color: var(--navy); font-weight: 700; font-size: 21px; line-height: 1.1; }
  .details .title { font-size: 17px; margin-top: 2px; }
  .details .address { font-size: 17px; line-height: 1.38; margin-top: 16px; }
  .details .contacts { list-style: none; margin-top: 14px; font-size: 17px; line-height: 1.38; }
  .details .contacts li { display: flex; align-items: center; gap: 7px; }
  .details .contacts svg { width: 12px; height: 12px; fill: var(--navy); flex: none; }
  .details .contacts .strong { color: var(--navy); }
</style>
</head>
<body>
<div class="canvas">
  <section class="card card-back">
    <div class="wordmark"><span>verra</span><span class="dot"></span></div>
  </section>

  <section class="card card-front">
    <div class="wordmark"><span>verra</span><span class="dot"></span></div>
    <div class="divider"></div>
    <div class="details">
      <p class="name">ELIAS MARLOW</p>
      <p class="title">President</p>
      <p class="address">215 Harbor Street, 3rd Floor<br>Ashford, NY 10481</p>
      <ul class="contacts">
        <li>
          <svg viewBox="0 0 24 24"><path d="M6.6 10.8a15 15 0 0 0 6.6 6.6l2.2-2.2a1 1 0 0 1 1-.25 11.4 11.4 0 0 0 3.6.57 1 1 0 0 1 1 1V20a1 1 0 0 1-1 1A17 17 0 0 1 3 4a1 1 0 0 1 1-1h3.5a1 1 0 0 1 1 1c0 1.25.2 2.45.57 3.57a1 1 0 0 1-.25 1z"/></svg>
          <span>555.014.2290</span>
        </li>
        <li>
          <svg viewBox="0 0 24 24"><path d="M2 5h20v14H2z M2 5l10 8 10-8" fill="none" stroke="#1b2b3f" stroke-width="2.4"/><path d="M2 5h20l-10 8z"/></svg>
          <span>sales@verrasupport.com</span>
        </li>
        <li>
          <svg viewBox="0 0 24 24"><g fill="none" stroke="#1b2b3f" stroke-width="2"><circle cx="12" cy="12" r="10"/><ellipse cx="12" cy="12" rx="4.5" ry="10"/><path d="M2 12h20M4 7h16M4 17h16"/></g></svg>
          <span>www.<span class="strong">verramanaged</span>.com</span>
        </li>
      </ul>
    </div>
  </section>
</div>
</body>
</html>
```